Stationery Design Project

Fire and building compliance company needs business card, letterhead and complement slip designed.
Have included a brief about business card, basic want front keep quite clean with just the MAS logo and the words Marbeck Alarm and Safety 2012 Ltd (small print) along the bottom. Website needs to be included (www.masalarm.example.nz) on either front or back.
The info for back is as per attachment.
Letterhead and complement slip should have the usual stuff MAS logo etc and also the accredited test lab logo at the bottom (can be small size)
Target Market(s)
Property owners, buisness managers
Industry/Entity Type
Building
Look and feel

```html
<!DOCTYPE html>
<html lang="en">
<head>
<meta charset="utf-8">
<title>MAS Business Card</title>
<link rel="stylesheet" href="https://fonts.googleapis.com/css2?family=Open+Sans:wght@400;600;700&display=swap">
<style>
  :root {
    --backdrop: #3b3b3d;
    --blue-light: #2b93c4;
    --blue-dark: #0b5680;
    --brand-blue: #1d5f87;
    --ink: #4a4a4c;
    --ink-soft: #6a6a6c;
    --rule: #d4d4d6;
    --badge: #1e2a5a;
    --white: #ffffff;
  }
  * { box-sizing: border-box; margin: 0; padding: 0; }
  html, body { width: 1200px; height: 900px; overflow: hidden; }
  body {
    background: var(--backdrop);
    font-family: "Open Sans", Arial, sans-serif;
    position: relative;
  }
  .card {
    position: absolute;
    left: 290px;
    width: 620px;
    height: 354px;
    border-radius: 3px;
    box-shadow: 0 12px 30px rgba(0,0,0,.45);
  }
  /* Back of card */
  .card-back {
    top: 50px;
    background: linear-gradient(135deg, var(--blue-light) 0%, #1b77a8 45%, var(--blue-dark) 100%);
    color: var(--white);
    text-align: center;
  }
  .back-brand {
    margin-top: 52px;
    display: flex;
    justify-content: center;
    align-items: center;
    gap: 12px;
  }
  .brand-dot {
    width: 34px; height: 34px; border-radius: 50%;
    background: var(--white);
  }
  .brand-name {
    font-size: 40px; font-weight: 700; letter-spacing: 1px; line-height: 1;
  }
  .back-tagline {
    font-size: 13px; margin-top: 6px; letter-spacing: .3px;
  }
  .services-title {
    font-size: 16px; font-weight: 700; margin-top: 22px;
  }
  .services-list {
    list-style: none; margin-top: 6px; font-size: 14px; line-height: 1.45;
  }
  .services-list li::before {
    content: ""; display: inline-block; width: 6px; height: 6px;
    border: 1.5px solid var(--white); border-radius: 50%;
    margin-right: 7px; vertical-align: middle;
  }
  /* Front of card */
  .card-front {
    top: 470px;
    background: var(--white);
    display: flex;
  }
  .front-brand-side {
    width: 50%;
    padding: 70px 0 0 50px;
    position: relative;
  }
  .front-brand {
    display: flex; align-items: center; gap: 14px;
  }
  .front-brand .brand-dot {
    width: 46px; height: 46px; background: var(--brand-blue);
  }
  .front-brand .brand-name {
    color: var(--ink); font-size: 58px;
  }
  .front-tagline {
    color: var(--ink-soft); font-size: 16px; margin: 6px 0 0 60px; line-height: 1.15;
  }
  .lab-badge {
    position: absolute; left: 50px; bottom: 48px;
    width: 54px; height: 62px;
    background: var(--badge);
    clip-path: polygon(50% 0, 100% 100%, 0 100%);
  }
  .divider {
    width: 1px; margin: 40px 0;
    background: linear-gradient(to bottom, transparent, var(--rule) 20%, var(--rule) 80%, transparent);
  }
  .contact-side {
    padding: 56px 0 0 30px; color: var(--ink);
  }
  .person-name {
    color: var(--brand-blue); font-size: 18px; font-weight: 700;
  }
  .person-role {
    font-size: 14px; color: var(--ink-soft); margin-bottom: 20px;
  }
  .contact-row {
    display: flex; align-items: flex-start; gap: 12px;
    font-size: 14px; line-height: 1.3; margin-bottom: 8px;
  }
  .contact-row strong { font-weight: 700; }
  .contact-icon { flex: 0 0 22px; height: 22px; }
</style>
</head>
<body>

<section class="card card-back" aria-label="Business card back">
  <div class="back-brand">
    <span class="brand-dot"></span>
    <span class="brand-name">MAS</span>
  </div>
  <p class="back-tagline">Fire and Building Compliance</p>
  <h2 class="services-title">Our services</h2>
  <ul class="services-list">
    <li>Building compliance specialists</li>
    <li>Building warrant of fitness preparation</li>
    <li>Fire alarms, Fire Extinguishers &amp;emergency lighting</li>
    <li>Approved evacuation schemes</li>
    <li>Pressure testing LPG CNG Fire extinguishers</li>
    <li>Security alarm and CCTV systems</li>
  </ul>
</section>

<section class="card card-front" aria-label="Business card front">
  <div class="front-brand-side">
    <div class="front-brand">
      <span class="brand-dot"></span>
      <span class="brand-name">MAS</span>
    </div>
    <p class="front-tagline">Fire and Building<br>Compliance</p>
    <div class="lab-badge" role="img" aria-label="Accredited laboratory badge"></div>
  </div>
  <div class="divider"></div>
  <div class="contact-side">
    <p class="person-name">Daniel Morrow</p>
    <p class="person-role">Operator</p>

    <div class="contact-row">
      <svg class="contact-icon" viewBox="0 0 22 22" aria-hidden="true"><circle cx="11" cy="11" r="11" fill="#1d5f87"/><path d="M11 5a4 4 0 0 0-4 4c0 3 4 8 4 8s4-5 4-8a4 4 0 0 0-4-4zm0 5.5a1.5 1.5 0 1 1 0-3 1.5 1.5 0 0 1 0 3z" fill="#fff"/></svg>
      <p><strong>Marbeck Alarm and Safety</strong><br>21 Harbour Lane Extension<br>Riverton, 4510</p>
    </div>
    <div class="contact-row">
      <svg class="contact-icon" viewBox="0 0 22 22" aria-hidden="true"><circle cx="11" cy="11" r="11" fill="#1d5f87"/><path d="M7.5 6h2l1 3-1.5 1a7 7 0 0 0 3 3l1-1.5 3 1v2a1.5 1.5 0 0 1-1.6 1.5A10 10 0 0 1 6 7.6 1.5 1.5 0 0 1 7.5 6z" fill="#fff"/></svg>
      <p>06 555 0182</p>
    </div>
    <div class="contact-row">
      <svg class="contact-icon" viewBox="0 0 22 22" aria-hidden="true"><circle cx="11" cy="11" r="11" fill="#1d5f87"/><rect x="6" y="8" width="10" height="7" rx="1" fill="#fff"/><rect x="8" y="5" width="6" height="4" fill="#fff"/><rect x="8" y="10" width="6" height="1" fill="#1d5f87"/></svg>
      <p>06 555 0147</p>
    </div>
    <div class="contact-row">
      <svg class="contact-icon" viewBox="0 0 22 22" aria-hidden="true"><circle cx="11" cy="11" r="11" fill="#1d5f87"/><rect x="5.5" y="7" width="11" height="8" rx="1" fill="#fff"/><path d="M5.5 7.5 11 12l5.5-4.5" stroke="#1d5f87" stroke-width="1.2" fill="none"/></svg>
      <p>admin@marbeck.example.nz</p>
    </div>
    <div class="contact-row">
      <svg class="contact-icon" viewBox="0 0 22 22" aria-hidden="true"><circle cx="11" cy="11" r="11" fill="#1d5f87"/><circle cx="11" cy="11" r="5.5" stroke="#fff" stroke-width="1.3" fill="none"/><path d="M5.5 11h11M11 5.5c-2.5 3-2.5 8 0 11M11 5.5c2.5 3 2.5 8 0 11" stroke="#fff" stroke-width="1.1" fill="none"/></svg>
      <p>www.masalarm.example.nz</p>
    </div>
  </div>
</section>

</body>
</html>
```